Refresh of Medical Website

We are wanting to revamp our website and add much more content to the site. Our current website is https://corvaleclinicwest.com.au/. We also want someone to be able to upload this to our server.

Target Market(s)

Medical

Coding

Coded - Design and coding required

Number of Pages Required

5+ page

Font styles to use
Sans Serif

Colors
85cae6
ecf7fb
fafcfe
3176b5

Requirements
Must have
• I will pride a document of all inspiration and additions we would like please contact me and I will provide this.

```html
<!DOCTYPE html>
<html lang="en">
<head>
<meta charset="utf-8">
<title>Corvale Clinic West — Ear Nose &amp; Throat Surgeon</title>
<link rel="stylesheet" href="https://fonts.googleapis.com/css2?family=Montserrat:wght@900&family=Work+Sans:wght@400;500&family=Roboto:wght@400;500&display=swap">
<style>
:root{
  --navy:#213d73;
  --navy-deep:#1d2b4c;
  --blue:#2f5aa8;
  --magenta:#962064;
  --magenta-ring:#b45b8f;
  --navy-ring:#4a6593;
  --green:#7fbe41;
  --orange:#f7a12e;
  --grey-bg:#f1f1f1;
  --topbar:#ececec;
  --text:#4a4a4a;
  --heading:#1b1b1b;
  --white:#ffffff;
}
*{box-sizing:border-box;margin:0;padding:0}
html,body{width:1200px;height:3863px;overflow:hidden}
body{position:relative;background:var(--white);font-family:'Roboto',sans-serif;color:var(--text)}
.abs{position:absolute}
.topbar{left:0;top:0;width:1200px;height:48px;background:var(--topbar);font-size:16px;color:#666;display:flex;align-items:center}
.topbar .addr{position:absolute;left:93px;display:flex;align-items:center;gap:8px}
.topbar .sep{position:absolute;left:440px;color:#999}
.topbar .phone{position:absolute;left:470px;display:flex;align-items:center;gap:8px;color:var(--blue);font-weight:500;font-size:18px}
.topbar .social{position:absolute;right:90px;display:flex;gap:18px}
.topbar .social span{width:12px;height:12px;border-radius:50%;background:#999}
.header{left:0;top:48px;width:1200px;height:92px;background:var(--white);display:flex;align-items:center;justify-content:center;gap:14px}
.brand-dot{width:46px;height:46px;border-radius:50%;background:var(--navy)}
.brand-name{font-family:'Work Sans',sans-serif;font-weight:500;font-size:34px;color:var(--navy);letter-spacing:-.5px}
.nav{left:0;top:140px;width:1200px;height:46px;background:var(--navy)}
.nav a{position:absolute;top:13px;transform:translateX(-50%);color:var(--white);font-size:16px;font-weight:500;text-decoration:none;white-space:nowrap}
.hero{left:0;top:186px;width:1200px;height:640px;background:linear-gradient(100deg,#233d6e 0%,#3a5a86 35%,#8da7be 60%,#6e8fb8 80%,#385b92 100%)}
.hero-title{left:88px;top:283px;font-family:'Montserrat',sans-serif;font-weight:900;font-size:60px;line-height:62px;color:var(--white)}
.hero-sub{left:89px;top:418px;width:560px;font-family:'Work Sans',sans-serif;font-size:22px;line-height:30px;color:var(--white)}
.btn{display:flex;align-items:center;justify-content:center;border-radius:30px;color:var(--white);font-weight:500;text-decoration:none}
.hero-btn{left:90px;top:505px;width:218px;height:54px;background:var(--blue);font-size:19px}
.feature{border-radius:50%;display:flex;flex-direction:column;align-items:center;text-align:center;color:var(--white)}
.feature h3{font-family:'Work Sans',sans-serif;font-weight:500;font-size:22px;margin:14px 0 10px}
.feature p{font-size:15px;line-height:26px;width:240px}
.feature.magenta{width:316px;height:316px;top:594px;background:var(--magenta);border:14px solid var(--magenta-ring);padding-top:54px}
.feature.navy{width:344px;height:344px;top:580px;left:428px;background:var(--navy);border:14px solid var(--navy-ring);padding-top:46px;z-index:2}
.intro-bg{left:0;top:826px;width:1200px;height:660px;background:var(--grey-bg)}
.intro-title{left:91px;top:970px;font-family:'Work Sans',sans-serif;font-weight:500;font-size:45px;line-height:53px;color:var(--heading);letter-spacing:.5px}
.rule{height:4px;width:40px;background:var(--navy)}
.intro-text{left:91px;top:1122px;width:594px;font-size:17px;line-height:33px;text-align:justify;color:#555}
.intro-btn{left:92px;top:1269px;width:163px;height:52px;background:var(--navy);font-size:16px}
.intro-mark{left:810px;top:980px;width:230px;height:230px;border-radius:50%;background:var(--navy)}
.sec-title{left:0;width:1200px;text-align:center;font-family:'Work Sans',sans-serif;font-weight:500;font-size:46px;color:var(--heading);letter-spacing:.5px}
.appt-intro{left:150px;top:1636px;width:900px;text-align:center;font-size:17px;line-height:32px;color:#555}
.appt{width:248px;height:248px;top:1712px;border-radius:50%;display:flex;flex-direction:column;align-items:center;justify-content:center;text-align:center;color:var(--white);font-size:17px;font-weight:500;line-height:23px;padding:0 34px}
.appt svg{margin-bottom:12px}
.clinic-photo{left:89px;top:2202px;width:356px;height:356px;border-radius:50%;background:radial-gradient(circle at 40% 35%,#7ab35a 0%,#5c8f4b 22%,#3d5f8c 50%,#8aa2c8 80%,#c9d6ea 100%)}
.clinic-title{left:592px;top:2122px;font-family:'Work Sans',sans-serif;font-weight:500;font-size:46px;color:var(--white);letter-spacing:.5px}
.clinic-text{left:592px;top:2230px;width:486px;font-size:17px;line-height:33px;color:var(--white);text-align:justify}
.clinic-btn{left:594px;top:2362px;width:226px;height:54px;background:var(--blue);font-size:17px}
.card{top:2751px;width:309px;height:400px;background:var(--white);box-shadow:0 3px 10px rgba(0,0,0,.15)}
.card .map{height:242px;background:linear-gradient(135deg,#e8ece9 0%,#dfe6e2 50%,#e6e8ee 100%)}
.card h4{font-family:'Work Sans',sans-serif;font-weight:500;font-size:23px;line-height:31px;color:var(--heading);margin:26px 19px 10px;letter-spacing:.3px}
.card p{font-size:16px;line-height:26px;color:#666;margin:0 19px}
.arrow{top:2942px;font-size:22px;color:#333}
.footer{left:0;top:3280px;width:1200px;height:583px}
.badge{top:3410px;height:58px;border-radius:6px;background:#e9ecf2;opacity:.85}
.pay{top:3528px;height:44px;width:238px;border-radius:6px;background:#e9ecf2;opacity:.85}
.soc{top:3618px;width:50px;height:50px;border-radius:50%;border:2px solid var(--white)}
.soc::after{content:"";position:absolute;left:19px;top:19px;width:8px;height:8px;border-radius:50%;background:var(--white)}
.flinks{left:0;width:1200px;text-align:center;color:var(--white);font-size:16px}
.flinks span{margin:0 14px}
.fcontact{left:0;top:3786px;width:1200px;text-align:center;color:var(--white);font-size:14px}
.copy{left:0;top:3826px;width:1200px;text-align:center;color:var(--white);font-size:14px}
.code{right:30px;top:3832px;color:var(--white);font-size:11px}
</style>
</head>
<body>

<div class="abs topbar">
  <div class="addr"><svg width="12" height="16" viewBox="0 0 12 16"><path d="M6 0a6 6 0 0 0-6 6c0 4.5 6 10 6 10s6-5.5 6-10a6 6 0 0 0-6-6zm0 8.5A2.5 2.5 0 1 1 6 3.5a2.5 2.5 0 0 1 0 5z" fill="#555"/></svg>52 Fernleigh Street Kessford, Victoria, 3550</div>
  <div class="sep">|</div>
  <div class="phone"><svg width="14" height="14" viewBox="0 0 24 24"><path d="M6.6 10.8a15 15 0 0 0 6.6 6.6l2.2-2.2a1 1 0 0 1 1-.25 11.4 11.4 0 0 0 3.6.57 1 1 0 0 1 1 1V20a1 1 0 0 1-1 1A17 17 0 0 1 3 4a1 1 0 0 1 1-1h3.5a1 1 0 0 1 1 1c0 1.25.2 2.45.57 3.6a1 1 0 0 1-.25 1z" fill="#2f5aa8"/></svg>03 5550 1234</div>
  <div class="social"><span></span><span></span><span></span><span></span></div>
</div>

<div class="abs header">
  <div class="brand-dot"></div>
  <div class="brand-name">Corvale Clinic West</div>
</div>

<nav class="abs nav">
  <a style="left:121px">About</a>
  <a style="left:247px">Our Clinic</a>
  <a style="left:410px">ENT Conditions</a>
  <a style="left:589px">Facial Plastics</a>
  <a style="left:778px">Patient Resources</a>
  <a style="left:945px">Booking</a>
  <a style="left:1072px">Contact</a>
</nav>

<div class="abs hero" role="img" aria-label="Photograph of the surgeon operating with a surgical microscope in theatre"></div>
<div class="abs intro-bg"></div>
<svg class="abs" style="left:0;top:760px" width="1200" height="70" viewBox="0 0 1200 70"><path d="M0 42 C300 50 600 20 900 10 C1050 6 1150 12 1200 20 L1200 70 L0 70Z" fill="#f1f1f1"/></svg>

<h1 class="abs hero-title">Ear Nose &amp;<br>Throat Surgeon</h1>
<p class="abs hero-sub">Our Goal is to deliver gold standard patient orientated care</p>
<a class="abs btn hero-btn">Get Started</a>

<div class="abs feature magenta" style="left:146px">
  <svg width="90" height="56" viewBox="0 0 90 56" fill="none" stroke="#fff" stroke-width="2.5"><circle cx="22" cy="14" r="8"/><circle cx="45" cy="12" r="9"/><circle cx="68" cy="14" r="8"/><path d="M6 50c0-12 7-20 16-20s16 8 16 20"/><path d="M28 52c0-13 8-22 17-22s17 9 17 22"/><path d="M52 50c0-12 7-20 16-20s16 8 16 20"/></svg>
  <h3>Our Team</h3>
  <p>Lorem ipsum dolor sit amet, consectetur adipiscing elit, sed do eiusmod tempor</p>
</div>
<div class="abs feature navy">
  <svg width="76" height="70" viewBox="0 0 76 70" fill="none" stroke="#fff" stroke-width="2.5"><rect x="3" y="8" width="58" height="52" rx="5"/><path d="M3 20h58M16 3v10M48 3v10"/><circle cx="17" cy="32" r="3"/><circle cx="31" cy="32" r="3"/><circle cx="45" cy="32" r="3"/><circle cx="17" cy="46" r="3"/><circle cx="31" cy="46" r="3"/><circle cx="58" cy="55" r="13" fill="#213d73"/><path d="M58 48v8h6"/></svg>
  <h3>Book an Appointment</h3>
  <p>Lorem ipsum dolor sit amet, consectetur adipiscing elit, sed do eiusmod tempor</p>
</div>
<div class="abs feature magenta" style="left:738px">
  <svg width="70" height="66" viewBox="0 0 70 66" fill="none" stroke="#fff" stroke-width="2.5"><rect x="18" y="14" width="34" height="50"/><rect x="3" y="30" width="15" height="34"/><rect x="52" y="30" width="15" height="34"/><path d="M35 2v10M30 7h10"/><rect x="24" y="22" width="6" height="6"/><rect x="40" y="22" width="6" height="6"/><rect x="24" y="34" width="6" height="6"/><rect x="40" y="34" width="6" height="6"/><rect x="30" y="50" width="10" height="14"/></svg>
  <h3>Our Clinic</h3>
  <p>Lorem ipsum dolor sit amet, consectetur adipiscing elit, sed do eiusmod tempor</p>
</div>

<h2 class="abs intro-title">Corvale Clinic West<br>Ear, Nose &amp; Throat Surgeon</h2>
<div class="abs rule" style="left:91px;top:1096px"></div>
<p class="abs intro-text">Established in Kessford in 2013, and now includes all of Victoria. Our goal is to deliver gold standard patient orientated care in Victoria. All ENT conditions are assessed by Mr Halden, and care is directed to achieve patient satisfaction.</p>
<a class="abs btn intro-btn">Read More</a>
<div class="abs intro-mark"></div>

<svg class="abs" style="left:0;top:1400px" width="1200" height="90" viewBox="0 0 1200 90"><path d="M0 78 C300 20 900 20 1200 78 L1200 90 L0 90Z" fill="#fff"/></svg>

<h2 class="abs sec-title" style="top:1530px">Your First Appointment</h2>
<div class="abs rule" style="left:580px;top:1604px"></div>
<p class="abs appt-intro">We want your experience with Corvale Clinic West to be a good one. To make things easier, please make sure you have the following with you.</p>

<div class="abs appt" style="left:90px;background:var(--blue)">
  <svg width="58" height="48" viewBox="0 0 58 48" fill="none" stroke="#fff" stroke-width="2.2"><path d="M3 18 29 3l26 15v27H3z"/><path d="M3 18l26 16 26-16"/><rect x="13" y="9" width="32" height="18"/></svg>
  Referral letter from your GP
</div>
<div class="abs appt" style="left:347px;background:var(--green)">
  <svg width="60" height="62" viewBox="0 0 60 62" fill="none" stroke="#fff" stroke-width="2.2"><path d="M30 3 55 12v18c0 15-11 26-25 30C16 56 5 45 5 30V12z"/><path d="M30 11 47 17v13c0 10-7 18-17 21-10-3-17-11-17-21V17z"/><path d="M25 22h10v7h7v10h-7v7H25v-7h-7V29h7z"/></svg>
  Medicare Card or private insurance details
</div>
<div class="abs appt" style="left:604px;background:var(--magenta);font-size:16px;line-height:22px;padding:0 22px">
  <svg width="60" height="50" viewBox="0 0 60 50" fill="none" stroke="#fff" stroke-width="2.2"><rect x="3" y="3" width="54" height="34"/><path d="M22 37v8M38 37v8M14 46h32M10 10h10M10 10v8M50 30H40M50 30v-8M30 14h18M30 20h18M30 26h10"/></svg>
  Current test results, relevant doctors letters and physical copies of any imaging (X-ray etc)
</div>
<div class="abs appt" style="left:861px;background:var(--orange)">
  <svg width="48" height="62" viewBox="0 0 48 62" fill="none" stroke="#fff" stroke-width="2.2"><rect x="3" y="7" width="42" height="52" rx="3"/><rect x="15" y="2" width="18" height="9" rx="2"/><path d="M20 18h8v6h6v8h-6v6h-8v-6h-6v-8h6z"/><path d="M11 46h26M11 52h26"/></svg>
  Current Medication List
</div>

<svg class="abs" style="left:0;top:2050px" width="1200" height="505" viewBox="0 0 1200 505"><path d="M0 72 C300 20 700 -5 1200 40 L1200 505 C900 430 500 400 0 500Z" fill="#213d73"/></svg>
<div class="abs clinic-photo" role="img" aria-label="Photograph of the surgeon in a green surgical cap looking through a microscope"></div>
<h2 class="abs clinic-title">Our Clinic</h2>
<div class="abs" style="left:592px;top:2200px;width:40px;height:4px;background:#fff"></div>
<p class="abs clinic-text">We want your experience with Corvale Clinic West to be a good one. To make things easier, please make sure you have the following with you.</p>
<a class="abs btn clinic-btn">Learn More</a>

<h2 class="abs sec-title" style="top:2636px">Our Locations</h2>
<div class="abs rule" style="left:580px;top:2712px"></div>

<div class="abs arrow" style="left:36px">‹</div>
<div class="abs arrow" style="left:1148px">›</div>

<div class="abs card" style="left:90px">
  <div class="map" role="img" aria-label="Street map marking the Tarrin clinic location"></div>
  <h4>Tarrin Specialist<br>Centre</h4>
  <p>18 Moreton Avenue Tarrin<br>Vic 3564</p>
</div>
<div class="abs card" style="left:446px">
  <div class="map" role="img" aria-label="Street map marking the Kessford consulting rooms"></div>
  <h4>Kessford Consulting<br>Rooms</h4>
  <p>52 Fernleigh Street Kessford Vic<br>3550</p>
</div>
<div class="abs card" style="left:802px">
  <div class="map" role="img" aria-label="Street map marking the Ardale hearing clinic"></div>
  <h4>Brightwell Hearing<br>Specialists Ardale</h4>
  <p>2/74 Juniper Avenue Ardale VIC<br>3500</p>
</div>

<svg class="abs footer" viewBox="0 0 1200 583"><path d="M0 72 C400 -10 800 -10 1200 72 L1200 583 L0 583Z" fill="#1d2b4c"/></svg>

<div class="abs badge" style="left:128px;width:136px"></div>
<div class="abs badge" style="left:306px;width:178px"></div>
<div class="abs badge" style="left:518px;width:160px"></div>
<div class="abs badge" style="left:746px;width:110px"></div>
<div class="abs badge" style="left:938px;width:130px"></div>

<div class="abs pay" style="left:354px"></div>
<div class="abs pay" style="left:608px"></div>

<div class="abs soc" style="left:483px"></div>
<div class="abs soc" style="left:544px"></div>
<div class="abs soc" style="left:605px"></div>
<div class="abs soc" style="left:666px"></div>

<div class="abs flinks" style="top:3704px"><span>About</span>|<span>Our Clinic</span>|<span>Booking</span>|<span>ENT Conditions</span></div>
<div class="abs flinks" style="top:3740px"><span>Facial Plastics</span>|<span>News &amp; Updates</span>|<span>Sitemap</span>|<span>Contact</span></div>
<div class="abs fcontact">52 Fernleigh Street Kessford, Victoria, 3550 &nbsp;|&nbsp; 03 5550 1234 &nbsp;|&nbsp; admin@corvaleclinicwest.com.au</div>
<div class="abs copy">Copyrights © 2021, The Company Name. All rights reserved.</div>
<div class="abs code">C28</div>

</body>
</html>
```